Business card design for a dynamic IT consulting company

We need a business card design for a young firm, specialized in the Telecommunications/Consulting industry. The name of the company is Dulmar and Partners Business Consulting Ltd. (Short name: Dulmar and Partnes)
Dulmar = solve read reverse, so we aim to be uncomplicated and solution-oriented. The small pipe in our logo is also related to the word solve. So we need a new business card design, which is simple, eye catching and something non traditional (I would probably prefer a square shaped design rather than a rectangle, but open for suggestions). Attached our logo.

Target Market(s)

Usually our customers are Tier1 Telecoms providers (Q-Linkor, Teravine, etc) and their executives.

Industry/Entity Type

Business

Contact Information for Business Card

Name: Gergely Tarnavedi
Email: g.tarnavedi@dulmar-example.hu
Web: www.dulmar-example.hu
Mobile: +36 30 555 0192
Title: Managing Director

Optional:
Company name: Dulmar and Partners Ltd.
Address: 1125 Budapest, Kovarhegyi str. 17/B, Hungary

Font styles to use
Other font styles liked:
• helveticaneue_medium, Prime Regular are used now.

Colors

Designer to choose colors to be used in the design.

Requirements
Must have
• I would like to have a 2 sided design.
Nice to have
• I thought if we make the logo a bit bigger (without the company name), that could go to the back with the company name below. I though, if the pipe in the logo is somehow touchable on the business card, would be nice and unique.

```html
<!DOCTYPE html>
<html lang="en">
<head>
<meta charset="utf-8">
<title>Dulmar – Business Card</title>
<link rel="stylesheet" href="https://fonts.googleapis.com/css2?family=Roboto+Condensed:wght@400;500&display=swap">
<style>
  :root {
    --page-bg: #e6e3df;
    --card-bg: #121212;
    --ink: #ffffff;
    --ink-soft: #d9d9d9;
    --magenta: #b0429a;
    --cyan: #1ea3dc;
  }
  * { margin: 0; padding: 0; box-sizing: border-box; }
  html, body {
    width: 1200px;
    height: 1200px;
    overflow: hidden;
    background: var(--page-bg);
    font-family: "Roboto Condensed", "Arial Narrow", sans-serif;
    color: var(--ink);
  }
  .canvas {
    width: 1200px;
    height: 1200px;
    display: flex;
    flex-direction: column;
    align-items: center;
    justify-content: center;
    gap: 70px;
  }
  .card {
    width: 840px;
    height: 480px;
    background: var(--card-bg);
    position: relative;
    box-shadow: 0 10px 28px rgba(0,0,0,0.18);
  }

  /* Shared name block */
  .brand {
    display: flex;
    align-items: center;
    gap: 18px;
  }
  .brand__mark {
    width: 22px;
    height: 22px;
    background: var(--magenta);
    flex: none;
  }
  .brand__name {
    font-weight: 400;
    font-size: 80px;
    line-height: 1;
    letter-spacing: 1px;
    color: var(--ink);
  }
  .descriptor {
    margin-top: 14px;
    font-size: 17px;
    letter-spacing: 8px;
    color: var(--ink);
  }

  /* Front side */
  .card--front {
    display: flex;
    flex-direction: column;
    align-items: center;
    justify-content: center;
  }
  .front-web {
    margin-top: 56px;
    font-size: 16px;
    letter-spacing: 3px;
    color: var(--ink-soft);
  }

  /* Back side */
  .back-brand {
    position: absolute;
    left: 60px;
    top: 60px;
    padding-left: 26px;
    border-left: 2px solid var(--ink);
  }
  .back-brand .brand__name { font-size: 64px; }
  .back-brand .brand__mark { width: 18px; height: 18px; }
  .back-brand .descriptor { font-size: 14px; letter-spacing: 6px; margin-top: 10px; }

  .person {
    position: absolute;
    left: 60px;
    bottom: 60px;
  }
  .person__name {
    font-size: 38px;
    font-weight: 400;
    line-height: 1.1;
  }
  .person__title {
    font-size: 20px;
    font-weight: 500;
    margin-top: 4px;
  }

  .contacts {
    position: absolute;
    right: 60px;
    bottom: 60px;
    list-style: none;
    display: flex;
    flex-direction: column;
    gap: 10px;
  }
  .contact {
    display: flex;
    align-items: flex-start;
    gap: 12px;
    font-size: 17px;
    line-height: 1.3;
  }
  .contact__square {
    width: 12px;
    height: 12px;
    margin-top: 5px;
    flex: none;
  }
  .contact__square--white { background: var(--ink); }
  .contact__square--magenta { background: var(--magenta); }
  .contact__square--cyan { background: var(--cyan); }
  .contact__icon {
    width: 18px;
    height: 18px;
    margin-top: 2px;
    flex: none;
  }
</style>
</head>
<body>
<main class="canvas">

  <section class="card card--front" aria-label="Card front">
    <div class="brand">
      <span class="brand__mark"></span>
      <span class="brand__name">Dulmar</span>
    </div>
    <p class="descriptor">BUSINESS CONSULTING</p>
    <p class="front-web">www.dulmar-example.hu</p>
  </section>

  <section class="card card--back" aria-label="Card back">
    <div class="back-brand">
      <div class="brand">
        <span class="brand__mark"></span>
        <span class="brand__name">Dulmar</span>
      </div>
      <p class="descriptor">BUSINESS CONSULTING</p>
    </div>

    <div class="person">
      <h1 class="person__name">Gergely Tarnavedi</h1>
      <p class="person__title">Managing Director</p>
    </div>

    <ul class="contacts">
      <li class="contact">
        <span class="contact__square contact__square--white"></span>
        <svg class="contact__icon" viewBox="0 0 18 18" aria-hidden="true">
          <path d="M9 1.5a5 5 0 0 0-5 5c0 3.8 5 10 5 10s5-6.2 5-10a5 5 0 0 0-5-5z" fill="#fff"/>
          <circle cx="9" cy="6.5" r="1.9" fill="#121212"/>
        </svg>
        <span>1125 Budapest, Kovarhegyi str.<br>17/B, Hungary</span>
      </li>
      <li class="contact">
        <span class="contact__square contact__square--magenta"></span>
        <svg class="contact__icon" viewBox="0 0 18 18" aria-hidden="true">
          <path d="M4.5 1.8l2.6 3.3-1.5 1.8c.9 2 2.4 3.6 4.4 4.6l1.8-1.5 3.4 2.5-1.2 3c-6.2-.3-11-5.2-11.3-11.5z" fill="#fff"/>
        </svg>
        <span>+36 30 555 0192</span>
      </li>
      <li class="contact">
        <span class="contact__square contact__square--cyan"></span>
        <svg class="contact__icon" viewBox="0 0 18 18" aria-hidden="true">
          <rect x="1.5" y="4" width="15" height="10.5" fill="none" stroke="#fff" stroke-width="1.6"/>
          <path d="M1.5 4l7.5 6 7.5-6" fill="none" stroke="#fff" stroke-width="1.6"/>
        </svg>
        <span>g.tarnavedi@dulmar-example.hu</span>
      </li>
      <li class="contact">
        <span class="contact__square contact__square--magenta"></span>
        <svg class="contact__icon" viewBox="0 0 18 18" aria-hidden="true">
          <circle cx="9" cy="9" r="7" fill="none" stroke="#fff" stroke-width="1.6"/>
          <ellipse cx="9" cy="9" rx="3" ry="7" fill="none" stroke="#fff" stroke-width="1.4"/>
          <path d="M2 9h14" stroke="#fff" stroke-width="1.4"/>
        </svg>
        <span>www.dulmar-example.hu</span>
      </li>
    </ul>
  </section>

</main>
</body>
</html>
```